Eye catching while remaining subtle, stylish and professional

Pellmore Works are a Heatpump and Air Conditioning Company. I would like stationary that would be suitable to use for letters, quoting invoicing. The final design should communicate a trade/service type industry that is clean and professional

I would like the designer to also offer a Business card option as well.

Details should include company logo as attached. Company details. Name, Address, Phone, Email and Website. You can use generic details until a final design is chosen

Target Market(s)

Trade/Service Industry

Industry/Entity Type

Air Conditioning

Requirements
Must have
• LOGO, Company contact details
Nice to have
• Watermark

```html
<!DOCTYPE html>
<html lang="en">
<head>
<meta charset="utf-8">
<title>Pellmore Works Stationery</title>
<link href="https://fonts.googleapis.com/css2?family=Jost:wght@400;500&family=Arimo:wght@400;700&display=swap" rel="stylesheet">
<style>
  :root {
    --bg: #eceeef;
    --paper: #ffffff;
    --brand: #2eaee5;
    --brand-light: #5cc6f0;
    --tab: #c9cacc;
    --ink: #3a3a3a;
    --ink-soft: #6b6b6b;
  }
  * { margin: 0; padding: 0; box-sizing: border-box; }
  html, body { width: 1200px; height: 937px; overflow: hidden; background: var(--bg); }
  .canvas { position: relative; width: 1200px; height: 937px; }
  .sheet { position: absolute; background: var(--paper); }
  .tab { position: absolute; top: 0; right: 0; background: var(--tab); }
  .wordmark {
    position: absolute; font-family: "Jost", sans-serif; font-weight: 500;
    color: var(--brand); text-transform: uppercase; white-space: nowrap;
    display: flex; align-items: center; gap: 6px;
  }
  .wordmark .dot { width: .55em; height: .55em; border-radius: 50%; background: var(--brand); }
  .band { position: absolute; display: flex; gap: 3px; }
  .band .seg {
    background: linear-gradient(180deg, var(--brand-light), var(--brand));
    display: flex; flex-direction: column; align-items: center; justify-content: center;
    color: #fff; font-family: "Arimo", sans-serif;
  }
  .band .seg:first-child { border-radius: 6px 0 0 6px; }
  .band .seg:last-child { border-radius: 0 6px 6px 0; }
  .band .icon { width: 11px; height: 11px; margin-bottom: 3px; }
  .band .small { font-size: 3.6px; line-height: 5px; text-align: center; }
  .web { font-family: "Arimo", sans-serif; letter-spacing: 2px; color: #fff; }

  /* letter */
  .letter { left: 185px; top: 66px; width: 385px; height: 546px; }
  .letter .tab { width: 95px; height: 14px; }
  .letter-body {
    position: absolute; left: 36px; top: 140px; width: 296px;
    font-family: "Arimo", sans-serif; font-size: 5.2px; line-height: 7.6px; color: var(--ink);
  }
  .letter-body p { margin-bottom: 7px; }
  .letter-body .gap { margin-bottom: 24px; }
  .letter-body strong { font-weight: 700; }
  .signature { width: 40px; height: 20px; background: #e4e4e4; margin: 4px 0 6px; }

  /* blank sheet */
  .plain { left: 636px; top: 41px; width: 459px; height: 576px; }
  .plain .tab { width: 98px; height: 16px; }

  /* cards */
  .card { width: 175px; height: 100px; }
  .card .tab { width: 62px; height: 8px; }
  .card-front { left: 46px; top: 658px; }
  .card-back { left: 46px; top: 785px; }
  .person { position: absolute; right: 10px; top: 20px; font-family: "Arimo", sans-serif; text-align: left; }
  .person .name { font-size: 7.5px; color: #222; letter-spacing: .5px; }
  .person .role { font-size: 4px; color: var(--ink-soft); font-weight: 700; }

  /* envelopes */
  .env-front { left: 265px; top: 672px; width: 432px; height: 208px; }
  .env-front .tab { width: 80px; height: 12px; }
  .env-back { left: 736px; top: 671px; width: 433px; height: 209px; }
  .flap { position: absolute; left: 0; top: 0; width: 433px; height: 72px; }
  .flap-web { position: absolute; left: 0; top: 28px; width: 100%; text-align: center; font-size: 13px; letter-spacing: 2.5px; color: #1c3a4a; font-family: "Arimo", sans-serif; }
</style>
</head>
<body>
<div class="canvas">

  <!-- Letterhead -->
  <section class="sheet letter">
    <div class="tab"></div>
    <div class="wordmark" style="left:36px; top:56px; font-size:21px;"><span class="dot"></span>Pellmore Works</div>
    <div class="letter-body">
      <p>July 2, 2012</p>
      <p><strong>Dear Sir,</strong><br>14 Kettle Lane, Harbour City</p>
      <p>Thank you for choosing Pellmore Works for your heating and cooling needs. Our team has visited the site and prepared a full quote for the supply and installation of a new heat pump system, including all fittings, wiring, testing and commissioning. Every unit we fit is backed by our service warranty, and a yearly maintenance plan is available to keep your system running quietly and efficiently through every season of the year ahead.</p>
      <p class="gap">Installation can begin within two weeks of your approval, and our technician will contact you to confirm a suitable time.</p>
      <p>Please review the attached quote and invoice terms at your convenience. Payment is due within fourteen days of completion, and we accept bank transfer or card. Should you have any questions about the units, the running costs or the install, our office team is happy to help by phone or email. We look forward to working with you and keeping your home comfortable all year round.</p>
      <p style="margin-bottom:2px;">Best Regards,</p>
      <div class="signature" role="img" aria-label="Handwritten signature"></div>
      <p><strong>Dana Whitfield</strong><br>Director<br><br>14 Kettle Lane, Harbour City</p>
    </div>
    <div class="band" style="left:8px; top:497px; width:370px; height:42px;">
      <div class="seg" style="width:109px;">
        <svg class="icon" viewBox="0 0 24 24"><path fill="#1f2b33" d="M3 9c0-2 4-4 9-4s9 2 9 4v2h-5V9H8v2H3zM7 12h10l2 7H5z"/><circle cx="12" cy="15.5" r="2" fill="#fff"/></svg>
        <div class="small">021 345 6789<br>021 345 6790</div>
      </div>
      <div class="seg" style="width:143px;">
        <svg class="icon" viewBox="0 0 24 24" fill="none" stroke="#1f2b33" stroke-width="2"><circle cx="12" cy="12" r="9"/><ellipse cx="12" cy="12" rx="4" ry="9"/><path d="M3 12h18M5 7h14M5 17h14"/></svg>
        <div class="small">info@pellmoreworks.com<br>service@pellmoreworks.com</div>
      </div>
      <div class="seg" style="width:112px;">
        <svg class="icon" viewBox="0 0 24 24"><path fill="#1f2b33" d="M12 2a7 7 0 0 0-7 7c0 5 7 13 7 13s7-8 7-13a7 7 0 0 0-7-7z"/><circle cx="12" cy="9" r="2.5" fill="#fff"/></svg>
        <div class="small">14 Kettle Lane<br>Harbour City</div>
      </div>
    </div>
  </section>

  <!-- Continuation sheet -->
  <section class="sheet plain">
    <div class="tab"></div>
    <div class="wordmark" style="left:0; width:100%; justify-content:center; top:266px; font-size:30px;"><span class="dot"></span>Pellmore Works</div>
    <div class="band" style="left:10px; top:541px; width:440px; height:22px;">
      <div class="seg" style="width:119px;"></div>
      <div class="seg" style="width:195px;"><span class="web" style="font-size:9px;">www.pellmoreworks.com</span></div>
      <div class="seg" style="width:116px;"></div>
    </div>
  </section>

  <!-- Business card front -->
  <section class="sheet card card-front">
    <div class="tab"></div>
    <div class="wordmark" style="left:9px; top:16px; font-size:8.5px; gap:3px;"><span class="dot"></span>Pellmore Works</div>
    <div class="person"><div class="name">OWEN CASTELL</div><div class="role">CREATIVE DIRECTOR</div></div>
    <div class="band" style="left:7px; top:45px; width:164px; height:52px;">
      <div class="seg" style="width:48px;">
        <svg class="icon" viewBox="0 0 24 24"><path fill="#1f2b33" d="M3 9c0-2 4-4 9-4s9 2 9 4v2h-5V9H8v2H3zM7 12h10l2 7H5z"/><circle cx="12" cy="15.5" r="2" fill="#fff"/></svg>
        <div class="small">021 345 6789<br>021 345 6790</div>
      </div>
      <div class="seg" style="width:63px;">
        <svg class="icon" viewBox="0 0 24 24" fill="none" stroke="#1f2b33" stroke-width="2"><circle cx="12" cy="12" r="9"/><ellipse cx="12" cy="12" rx="4" ry="9"/><path d="M3 12h18M5 7h14M5 17h14"/></svg>
        <div class="small">info@pellmoreworks.com<br>service@pellmoreworks.com</div>
      </div>
      <div class="seg" style="width:47px;">
        <svg class="icon" viewBox="0 0 24 24"><path fill="#1f2b33" d="M12 2a7 7 0 0 0-7 7c0 5 7 13 7 13s7-8 7-13a7 7 0 0 0-7-7z"/><circle cx="12" cy="9" r="2.5" fill="#fff"/></svg>
        <div class="small">14 Kettle Lane<br>Harbour City</div>
      </div>
    </div>
  </section>

  <!-- Business card back -->
  <section class="sheet card card-back">
    <div class="tab"></div>
    <div class="wordmark" style="left:9px; top:65px; font-size:9px; gap:3px;"><span class="dot"></span>Pellmore Works</div>
  </section>

  <!-- Envelope front -->
  <section class="sheet env-front">
    <div class="tab"></div>
    <div class="wordmark" style="left:32px; top:42px; font-size:19px;"><span class="dot"></span>Pellmore Works</div>
    <div class="band" style="left:14px; top:176px; width:402px; height:21px;">
      <div class="seg" style="width:112px;"></div>
      <div class="seg" style="width:171px;"><span class="web" style="font-size:9px;">www.pellmoreworks.com</span></div>
      <div class="seg" style="width:113px;"></div>
    </div>
  </section>

  <!-- Envelope back -->
  <section class="sheet env-back">
    <svg class="flap" viewBox="0 0 433 72" aria-hidden="true">
      <defs>
        <linearGradient id="flapFill" x1="0" y1="0" x2="0" y2="1">
          <stop offset="0" stop-color="#6fd0f4"/>
          <stop offset="1" stop-color="#2eaee5"/>
        </linearGradient>
      </defs>
      <path d="M0 0H433V28Q433 72 389 72H44Q0 72 0 28Z" fill="url(#flapFill)"/>
    </svg>
    <div class="flap-web">www.pellmoreworks.com</div>
  </section>

</div>
</body>
</html>
```